Halvorsen Chiropractic we would like to design a trifold brochure that highlights our services

We need a Trifold created for our Chiropractic offices that highlights our services and treatments that we offer giving patients a better quality of life . Areas to highlight
conditions can be found on our websites and specialties .www.halvorsenchiropractic.example
our doctors have over 20 years experience in this field .
they have worked with the Ridgeback Falcons and Dr. Ned Halvorsen is the Marlowe Crest university basketball teams main chiropractor.

Target Market(s)

children to elderly

Font styles to use
Serif

Colors
00a990
0255a3

Requirements
Must have
• logo
• contact info
• pics of doctors
• bios of doctors
• location
• services provided
Nice to have
• none
Should not have
• do not use picture on website of staff we have all new staff in office

```html
<!DOCTYPE html>
<html lang="en">
<head>
<meta charset="utf-8">
<title>Halvorsen Chiropractic – Trifold Brochure</title>
<link rel="stylesheet" href="https://fonts.googleapis.com/css2?family=Cinzel:wght@700&family=PT+Serif:ital,wght@0,400;0,700;1,400&display=swap">
<style>
  :root {
    --teal: #00a990;
    --blue: #0255a3;
    --navy: #0a3f86;
    --ink: #2b3440;
    --paper: #ffffff;
    --mist: #eef1f4;
    --backdrop: #e4e8ec;
    --photo-a: #c9d3dc;
    --photo-b: #8fa2b4;
    --link: #7fe3d3;
  }
  * { box-sizing: border-box; margin: 0; padding: 0; }
  html, body { width: 1200px; height: 990px; overflow: hidden; }
  body {
    background: var(--backdrop);
    font-family: "PT Serif", Georgia, serif;
    color: var(--ink);
  }
  .brochure {
    position: absolute;
    left: 30px; top: 55px;
    width: 1140px; height: 880px;
    display: flex;
    box-shadow: 0 10px 30px rgba(0,0,0,.18);
  }
  .panel {
    position: relative;
    width: 380px; height: 880px;
    overflow: hidden;
    background: var(--paper);
  }
  .panel + .panel { border-left: 1px solid rgba(0,0,0,.06); }
  .decor { position: absolute; left: 0; top: 0; width: 380px; height: 880px; }
  .content { position: relative; z-index: 1; }

  /* Shared type */
  .section-banner {
    display: inline-block;
    background: var(--blue);
    color: #fff;
    font-family: "Cinzel", "Times New Roman", serif;
    font-weight: 700;
    font-size: 17px;
    letter-spacing: .5px;
    padding: 5px 22px 5px 34px;
    border-radius: 0 18px 18px 0;
    margin: 0 0 10px -30px;
  }
  .body-copy {
    font-size: 11.2px;
    line-height: 1.42;
    text-align: justify;
    margin-bottom: 8px;
  }
  .body-copy strong { color: var(--blue); }

  /* Left panel */
  .panel--benefits .content { padding: 92px 30px 0 30px; }
  .testimonial {
    font-size: 11px;
    line-height: 1.42;
    text-align: justify;
    font-style: italic;
    margin-bottom: 4px;
  }
  .testimonial::before {
    content: "\201C";
    color: var(--teal);
    font-size: 22px;
    font-style: normal;
    line-height: 0;
    vertical-align: -7px;
    margin-right: 2px;
  }
  .testimonial-source {
    text-align: right;
    font-size: 11px;
    font-weight: 700;
    color: var(--blue);
    margin-bottom: 10px;
  }

  /* Middle panel */
  .brand {
    position: absolute; top: 44px; left: 0; width: 380px;
    display: flex; align-items: center; justify-content: center; gap: 12px;
    z-index: 1;
  }
  .brand-dot {
    width: 34px; height: 34px; border-radius: 50%;
    background: var(--teal);
  }
  .brand-name {
    font-family: "Cinzel", "Times New Roman", serif;
    font-weight: 700;
    font-size: 24px;
    line-height: 1.05;
    color: var(--blue);
  }
  .panel--lead .content { padding: 170px 28px 0 28px; color: #fff; }
  .doctor-photo {
    width: 150px; height: 150px;
    border: 5px solid #fff;
    border-radius: 12px;
    background: linear-gradient(160deg, var(--photo-a), var(--photo-b));
    box-shadow: 0 4px 10px rgba(0,0,0,.25);
    margin: 0 auto 12px;
  }
  .doctor-name {
    font-family: "Cinzel", "Times New Roman", serif;
    font-weight: 700;
    font-size: 20px;
    text-align: center;
    margin-bottom: 10px;
  }
  .panel--lead .doctor-name { color: #fff; }
  .panel--lead .body-copy { color: #fff; font-size: 11px; }
  .panel--lead .body-copy strong { color: var(--link); }
  .lead-quote {
    font-size: 11px; line-height: 1.42; text-align: justify;
    font-style: italic; color: #fff; margin-top: 6px;
  }
  .website {
    position: absolute; left: 0; bottom: 52px; width: 380px;
    text-align: center;
    font-size: 15px; font-weight: 700;
    color: var(--link);
    z-index: 1;
  }

  /* Right panel */
  .panel--associate { background: linear-gradient(180deg, var(--paper) 0%, var(--mist) 100%); }
  .panel--associate .content { padding: 92px 30px 0 30px; }
  .panel--associate .doctor-photo { width: 150px; height: 150px; margin-bottom: 10px; }
  .panel--associate .doctor-name { color: var(--navy); font-size: 21px; margin-bottom: 8px; }
  .panel--associate .body-copy { font-size: 10.8px; line-height: 1.4; margin-bottom: 6px; }
  .panel--associate .section-banner { font-size: 15px; margin: 4px 0 6px -30px; padding-top: 3px; padding-bottom: 3px; }
  .services-list {
    list-style: none;
    display: grid;
    grid-template-columns: 1fr 1fr;
    column-gap: 10px;
    row-gap: 2px;
    font-size: 11px;
    line-height: 1.4;
    margin-bottom: 8px;
  }
  .services-list li::before {
    content: "\2713";
    color: var(--teal);
    font-weight: 700;
    margin-right: 6px;
  }
  .contact {
    width: 160px;
    font-size: 10.8px;
    line-height: 1.4;
    color: var(--navy);
  }
  .contact-line { display: flex; gap: 6px; align-items: flex-start; }
  .contact-line + .contact-line { margin-top: 3px; }
  .contact-icon { flex: 0 0 12px; width: 12px; height: 12px; margin-top: 2px; }
  .contact-phone { font-weight: 700; }
  .care-images {
    position: absolute; bottom: 16px; right: 30px; display: flex; gap: 8px; z-index: 1;
  }
  .care-image {
    width: 80px; height: 80px; border-radius: 50%;
    border: 4px solid #fff;
    box-shadow: 0 3px 8px rgba(0,0,0,.2);
  }
  .care-image--spine { background: radial-gradient(circle at 50% 45%, #e0863a, #1f4f8e 70%); }
  .care-image--head { background: radial-gradient(circle at 55% 45%, #e24b2e, #f2c9a6 45%, #f4efe9 80%); }
</style>
</head>
<body>
<main class="brochure">

  <!-- Left panel: benefits + testimonials -->
  <section class="panel panel--benefits">
    <svg class="decor" viewBox="0 0 380 880" aria-hidden="true">
      <path d="M0 0 H230 C170 20 90 40 0 95 Z" fill="var(--teal)"/>
      <path d="M0 0 H150 C100 25 50 50 0 70 Z" fill="var(--blue)"/>
      <path d="M0 880 V810 C120 760 250 790 380 740 V880 Z" fill="var(--teal)"/>
      <path d="M0 880 V835 C130 800 260 830 380 780 V880 Z" fill="var(--blue)"/>
    </svg>
    <div class="content">
      <h2 class="section-banner">The Benefits of Chiropractic</h2>
      <p class="body-copy">Many people in Nashville have the idea that <strong>chiropractic care</strong> is just a great way to treat back and neck pain. While it's true that chiropractic is far better than medical care for such problems, our job at Halvorsen Chiropractic is to help you improve your overall health and wellness.</p>
      <p class="body-copy">Your body has an incredible, innate ability to heal itself and be well. When your body isn't functioning properly, you experience illness, disease, or pain.</p>
      <p class="body-copy">Every function of your body is controlled by your central nervous system, and this function can be disrupted by misalignments in your spine. These are called <strong>subluxations</strong>. A subluxation creates interference in the function of your spinal nerves, and this can result in impaired functioning of your organs and endocrine system.</p>
      <p class="body-copy">Chiropractic adjustments are simply a way to remove that interference and restore the natural function of your body. Chiropractic is truly about prevention.</p>

      <h2 class="section-banner">Testimonials</h2>
      <p class="testimonial">Dr. Halvorsen has played such an integral role in my recovery and I would highly recommend him for his sound judgment, caring nature, and dedication to his patients. Dr. Halvorsen is leading the path here in Nashville!”</p>
      <p class="testimonial-source">– sunnyday17 at LocalReview</p>
      <p class="testimonial">I am a runner and Dr. Halvorsen has helped me on the road and off the injured list. I have had a couple of overuse injuries that he was able to diagnose and fix quickly. He administered deep tissue massage therapy, chiropractic adjustments and stretching. He also taught me some strengthening and exercise techniques to do on my own. I would recommend Dr. Halvorsen to anyone suffering from injury or overuse aches and pains. He will help you!”</p>
      <p class="testimonial-source">– Maren-Nashville</p>
    </div>
  </section>

  <!-- Middle panel: brand + lead doctor -->
  <section class="panel panel--lead">
    <svg class="decor" viewBox="0 0 380 880" aria-hidden="true">
      <path d="M0 118 C120 150 260 95 380 130 V880 H0 Z" fill="var(--teal)"/>
      <path d="M0 132 C120 168 260 110 380 148 V880 H0 Z" fill="var(--blue)"/>
      <path d="M0 860 C120 820 260 870 380 830 V880 H0 Z" fill="var(--teal)"/>
      <path d="M0 872 C120 840 260 885 380 852 V880 H0 Z" fill="var(--paper)"/>
    </svg>
    <div class="brand">
      <span class="brand-dot"></span>
      <span class="brand-name">Halvorsen<br>Chiropractic</span>
    </div>
    <div class="content">
      <div class="doctor-photo" role="img" aria-label="Portrait photo of Dr. Ned Halvorsen"></div>
      <h1 class="doctor-name">Dr. Ned Halvorsen</h1>
      <p class="body-copy">Since Dr. Halvorsen was old enough to dream, he knew that he wanted to be a chiropractor. After attending Westbrook College of Chiropractic West and fueling his passion for chiropractic with the mindset of putting patients first, he has made the dream of owning his own practice in Nashville a reality. Dr. Ned offers a range of therapies so that each patient leaves feeling rejuvenated, with a plan built for his or her individual needs.</p>
      <p class="body-copy">With <strong>over 20 years of experience</strong>, our doctors have worked with the <strong>Ridgeback Falcons</strong>, and Dr. Ned is the main chiropractor for the <strong>Marlowe Crest University</strong> basketball team.</p>
      <p class="lead-quote">“No one leaves this clinic feeling like a number,” comments Dr. Ned. “I don't want you to only feel better for a day after you see me. I want you to feel better indefinitely by receiving a wellness plan that I have specifically designed for you. Every person that walks through these doors is different. My goal is to promote healthy habits along with patient therapies so that pain will not be an option.”</p>
    </div>
    <p class="website">www.halvorsenchiropractic.example</p>
  </section>

  <!-- Right panel: associate doctor, services, contact -->
  <section class="panel panel--associate">
    <svg class="decor" viewBox="0 0 380 880" aria-hidden="true">
      <path d="M380 0 H150 C220 25 300 45 380 100 Z" fill="var(--teal)"/>
      <path d="M380 0 H230 C280 25 330 45 380 70 Z" fill="var(--blue)"/>
      <path d="M0 880 V820 C110 850 250 790 380 780 V880 Z" fill="var(--teal)"/>
      <path d="M0 880 V845 C120 870 260 820 380 815 V880 Z" fill="var(--blue)"/>
    </svg>
    <div class="content">
      <div class="doctor-photo" role="img" aria-label="Portrait photo of Dr. Jonas Halvorsen"></div>
      <h1 class="doctor-name">Dr. Jonas Halvorsen</h1>
      <p class="body-copy">Dr. Jonas Halvorsen is originally from Michigan. He earned his Bachelors of Science from Ashgrove University in Ithaca, NY and his Doctorate of Chiropractic from Westbrook College of Chiropractic West in San Jose, CA, completing his internship at Harbor Light Ministry and Open Hands Outreach's Community Outreach Program.</p>
      <p class="body-copy">Specializing in spinal and extremity rehabilitation, Dr. Jon cares for everyone from children to athletes and seniors. His main passion is to educate his patients about how to treat, prevent, and overcome injuries.</p>
      <p class="body-copy">Dr. Jon has now relocated back to Nashville, Tennessee to join his brother at Halvorsen Chiropractic, using myofascial release, rehabilitation, exercise, nutrition, and physiotherapy to treat his patients' conditions.</p>

      <h2 class="section-banner">Our Services</h2>
      <ul class="services-list">
        <li>Spinal adjustments</li>
        <li>Sports injury care</li>
        <li>Pediatric chiropractic</li>
        <li>Senior wellness care</li>
        <li>Myofascial release</li>
        <li>Rehab &amp; nutrition</li>
      </ul>

      <address class="contact">
        <div class="contact-line">
          <svg class="contact-icon" viewBox="0 0 12 12" aria-hidden="true"><path d="M6 0.5 C3.6 0.5 2 2.2 2 4.4 C2 7.2 6 11.5 6 11.5 C6 11.5 10 7.2 10 4.4 C10 2.2 8.4 0.5 6 0.5 Z" fill="var(--teal)"/><circle cx="6" cy="4.4" r="1.5" fill="#fff"/></svg>
          <span>1420 Maple Ridge Ave, Suite 200<br>Nashville, TN 37203</span>
        </div>
        <div class="contact-line">
          <svg class="contact-icon" viewBox="0 0 12 12" aria-hidden="true"><path d="M2.6 0.8 L4.4 0.8 L5.2 3.4 L4 4.4 C4.7 5.9 6.1 7.3 7.6 8 L8.6 6.8 L11.2 7.6 L11.2 9.4 C11.2 10.4 10.4 11.2 9.4 11.2 C4.7 11.2 0.8 7.3 0.8 2.6 C0.8 1.6 1.6 0.8 2.6 0.8 Z" fill="var(--teal)"/></svg>
          <span class="contact-phone">(615) 555-0148</span>
        </div>
      </address>
    </div>
    <div class="care-images">
      <div class="care-image care-image--spine" role="img" aria-label="Illustration of a human spine highlighted in orange"></div>
      <div class="care-image care-image--head" role="img" aria-label="Illustration of a head with a highlighted area of pain"></div>
    </div>
  </section>

</main>
</body>
</html>
```